Business Card Design job - Tyre Shop

Client wants a double sided business cards designed for a Tyre Shop.

The logo can be used in multiple ways, some examples are attached.

The reference font is:
https://www.typebarrel.example/fonts/open-sans
Others can be applied.

Color scheme should be mainly black and white, and red as a third less used color.

Contact Information for Business Card

Required Fields (Portuguese language):
- Name "Artur Maldo"
- Title "Gerente"
- Phone "256 907 342"
- Website "www.rodalimpa.pt"
- Email "geral@rodalimpa.pt
- Address "Rua das Feiteiras N.187
4790-318 Quintela, Vizela"

Font styles to use
Sans Serif

Requirements
Must have
• Corporate Logo
Nice to have
• The client would like the card to have special feature to measure the tyre tread, as shown in examples attached.
• The tread Values as Portuguese law are:
• - Ilegal - less than 1.6mm
• - change tyres - between 3mm and 1.6 mm
• - OK - above 3mm
• Card should be kept standard rectangle size 85x55mm

```html
<!DOCTYPE html>
<html lang="pt">
<head>
<meta charset="utf-8">
<title>Roda Limpa – Cartão de Visita</title>
<link rel="stylesheet" href="https://fonts.googleapis.com/css2?family=Open+Sans:wght@400;600;700;800&display=swap">
<style>
  :root {
    --stage: #b4b4b4;
    --card-white: #ffffff;
    --card-black: #070405;
    --ink: #111111;
    --accent-red: #e8202a;
    --tread-light: #f0f1f1;
    --tread-faint: #f1f1f1;
  }
  * { margin: 0; padding: 0; box-sizing: border-box; }
  html, body {
    width: 1200px; height: 1200px; overflow: hidden;
    background: var(--stage);
    font-family: "Open Sans", Arial, sans-serif;
  }
  .stage { position: relative; width: 1200px; height: 1200px; }

  .card { position: absolute; width: 576px; height: 344px; overflow: hidden; }
  .card--front { left: 154px; top: 228px; background: var(--card-white); color: var(--ink); }
  .card--back { left: 462px; top: 619px; background: var(--card-black); }

  .card__decor { position: absolute; inset: 0; }

  .accent-block {
    position: absolute; left: 0; top: 60px; width: 30px; height: 43px;
    background: var(--accent-red);
  }
  .identity { position: absolute; left: 38px; top: 50px; }
  .identity__name { font-size: 30px; font-weight: 700; line-height: 1.15; letter-spacing: 0.2px; }
  .identity__title { font-size: 19px; font-weight: 400; line-height: 1.1; }

  .contact { position: absolute; left: 38px; top: 210px; font-size: 16px; line-height: 19.5px; }
  .contact__address { margin-bottom: 19px; }
  .contact__label { font-weight: 700; }

  .brand-name {
    position: absolute; font-weight: 800; text-transform: uppercase; line-height: 1;
    white-space: nowrap;
  }
  .card--front .brand-name {
    right: 40px; top: 48px; font-size: 26px; color: var(--ink); text-align: left;
  }
  .card--back .brand-name {
    left: 126px; top: 159px; font-size: 30px; letter-spacing: -0.5px; color: var(--card-white);
  }
</style>
</head>
<body>
<main class="stage">

  <section class="card card--front" aria-label="Frente do cartão">
    <svg class="card__decor" width="576" height="344" viewBox="0 0 576 344" role="img" aria-label="Padrão de piso de pneu em tom claro">
      <path d="M576 140 C520 190 470 260 340 344 L576 344 Z" fill="var(--tread-faint)"/>
    </svg>
    <div class="accent-block"></div>
    <div class="identity">
      <div class="identity__name">Artur Maldo</div>
      <div class="identity__title">Gerente</div>
    </div>
    <div class="brand-name">Roda<br>Limpa</div>
    <div class="contact">
      <p class="contact__address">Rua das Feiteiras N.187<br>4790-318 Quintela, Vizela</p>
      <p><span class="contact__label">Phone:</span> 256 907 342</p>
      <p><span class="contact__label">Email:</span> geral@rodalimpa.pt</p>
      <p><span class="contact__label">Web:</span> www.rodalimpa.pt</p>
    </div>
  </section>

  <section class="card card--back" aria-label="Verso do cartão">
    <svg class="card__decor" width="576" height="344" viewBox="0 0 576 344" role="img" aria-label="Padrão de piso de pneu em grande escala">
      <path d="M408 0 L576 0 L576 344 L242 344 C300 300 360 220 408 0 Z" fill="var(--tread-light)"/>
    </svg>
    <div class="brand-name">Roda Limpa</div>
  </section>

</main>
</body>
</html>
```